4D Hush Little Nest Luxury Ultrasound Billboard

Design a HIGH-END, MODERN billboard for my private prenatal ultrasound studio, 4D Hush Little Nest, located in Pace, Florida.
This billboard will be viewed by drivers traveling at highway speeds, so it must be extremely clean, simple, and readable within 6 seconds.
About My Business
4D Hush Little Nest is a private prenatal ultrasound studio specializing in:
Highest technology 4D/HD Ultrasounds
Early Gender Determination
Pregnancy Confirmation
I have been serving families for nearly 10 years and is known for creating a memorable experience, not just an ultrasound appointment.
Design Style
I DO NOT want:
Flowers
Leaves
Swirls
Glitter
Hearts everywhere
Busy backgrounds
Generic maternity stock graphics
I DO want:
Modern
Luxury
Upscale
Clean
Professional
Eye-catching
Premium medical spa feel
Colors
Use colors from my logo:
LOGO Green ( or a deep green)
Black
White
Soft Gold accents
Images:
Incorporate my professional headshot in a clean, modern way, logo, and the ultrasound images
Text
Keep wording minimal.
Primary Headline ( OPEN TO IDEAS) :
EXAMPLES ( WOULD RATHER SOMETHING MORE CATCHY)
" ADVANCED IMAGING. UNFORGETTABLE MOMENTS"
"MEET YOUR BABY BEFORE BIRTH"
Under headline:
4D Ultrasound • Early Gender • Pregnancy Confirmation
Business Name:
4D Hush Little Nest
Private Prenatal Ultrasound Studio
Phone Number:
850-471-3905
Important
This billboard must be readable in 5–6 seconds from a moving vehicle.
Less text is better.
The phone number and business name must be visible from a distance.
The design should feel like a premium brand that immediately tells expecting parents:
“This is where I go to see my baby.”
Files Provided
Official logo
Headshot
Ultrasound images
Don’t make this look like a medical office billboard.
Make it look like a luxury baby experience billboard. That’s what separates 4D Hush Little Nest from hospitals, OB offices, and all the new studios popping up around you. The emotional connection is what gets moms to book. ❤️
Billboard Size - 10.6” x 36”

```html
<!DOCTYPE html>
<html lang="en">
<head>
<meta charset="UTF-8">
<title>4D Hush Little Nest – Billboard</title>
<link rel="stylesheet" href="https://fonts.googleapis.com/css2?family=Oswald:wght@300;600&family=Signika:wght@600;700&display=swap">
<style>
  :root {
    --gold: #d3a63c;
    --slate: #5a646b;
    --ink: #2f3439;
    --white: #ffffff;
    --page: #eceeef;
    --scrub-green: #2f4a30;
    --hair: #c9a56e;
    --screen: #2a2523;
    --scan: #b26a45;
  }
  * { margin: 0; padding: 0; box-sizing: border-box; }
  html, body { width: 1200px; height: 1200px; overflow: hidden; background: var(--page); }
  .billboard {
    position: absolute; left: 0; top: 423px;
    width: 1200px; height: 354px;
    background: var(--white);
    overflow: hidden;
    box-shadow: 0 10px 24px rgba(0,0,0,0.25);
    font-family: "Signika", sans-serif;
  }
  .billboard-shapes { position: absolute; inset: 0; }
  .label {
    position: absolute; color: var(--ink); font-weight: 700;
    line-height: 1; white-space: nowrap;
  }
  .headline {
    position: absolute; color: var(--gold);
    font-family: "Oswald", sans-serif; font-weight: 300;
    line-height: 1; white-space: nowrap; letter-spacing: -1px;
  }
  .studio-type { left: 28px; top: 40px; font-size: 21px; line-height: 1.05; text-align: center; width: 180px; white-space: normal; }
  .brand-name {
    position: absolute; left: 28px; top: 112px; width: 172px;
    font-family: "Signika", sans-serif; font-weight: 700;
    font-size: 30px; line-height: 1.05; color: var(--gold); text-align: center;
  }
  .lead-advanced { left: 230px; top: 50px; font-size: 24px; }
  .word-imaging { left: 228px; top: 72px; font-size: 64px; }
  .lead-unforgettable { left: 227px; top: 152px; font-size: 24px; }
  .word-moments { left: 228px; top: 174px; font-size: 64px; }
  .services { position: absolute; color: var(--ink); font-weight: 700; font-size: 27px; line-height: 1; white-space: nowrap; }
  .services-top { left: 715px; top: 22px; }
  .services-bottom { left: 758px; top: 66px; }
  .services .dot { display: inline-block; width: 22px; height: 22px; border-radius: 50%; background: var(--ink); margin-right: 6px; vertical-align: -2px; }
  .services .dot + .dot, .gap { margin-left: 10px; }
  .lead-meet { left: 1000px; top: 133px; font-size: 22px; }
  .word-baby { left: 998px; top: 156px; font-size: 66px; }
  .lead-before { left: 1000px; top: 236px; font-size: 22px; }
  .word-birth { left: 998px; top: 258px; font-size: 66px; }
  .phone {
    position: absolute; left: 37px; top: 282px; display: flex; align-items: center; gap: 12px;
  }
  .phone-icon { width: 48px; height: 48px; }
  .phone-number {
    font-family: "Oswald", sans-serif; font-weight: 600; color: var(--white);
    font-size: 50px; line-height: 1; letter-spacing: 0.5px;
  }
</style>
</head>
<body>
<section class="billboard">
  <svg class="billboard-shapes" width="1200" height="354" viewBox="0 0 1200 354">
    <defs>
      <linearGradient id="headshot-tone" x1="0" y1="0" x2="0" y2="1">
        <stop offset="0" stop-color="var(--hair)"/>
        <stop offset="0.45" stop-color="#b99473"/>
        <stop offset="1" stop-color="var(--scrub-green)"/>
      </linearGradient>
      <linearGradient id="machine-tone" x1="0" y1="0" x2="0" y2="1">
        <stop offset="0" stop-color="var(--screen)"/>
        <stop offset="0.55" stop-color="#3a3532"/>
        <stop offset="1" stop-color="#cfd1d0"/>
      </linearGradient>
    </defs>
    <path class="slate-wave" fill="var(--slate)"
      d="M0 248 C 70 236, 170 240, 300 262 C 420 282, 520 286, 640 282 C 760 280, 900 268, 980 288 C 1020 300, 1040 330, 1045 354 L0 354 Z"/>
    <path class="gold-band" fill="var(--gold)"
      d="M665 0 C 700 60, 740 104, 830 112 C 960 120, 1100 124, 1200 146 L1200 0 Z"/>
    <rect class="headshot" x="494" y="10" width="214" height="344" rx="90" fill="url(#headshot-tone)"
      role="img" aria-label="Portrait of the studio sonographer in green scrubs holding an ultrasound probe"/>
    <rect class="ultrasound-machine" x="708" y="120" width="190" height="234" rx="10" fill="url(#machine-tone)"
      role="img" aria-label="Ultrasound machine whose screen shows a 4D scan of twin babies face to face"/>
    <rect x="722" y="134" width="162" height="112" rx="4" fill="var(--scan)" opacity="0.55"/>
  </svg>

  <p class="label studio-type">Private Prenatal Ultrasound Studio</p>
  <p class="brand-name">4D Hush Little Nest</p>

  <p class="label lead-advanced">ADVANCED</p>
  <p class="headline word-imaging">IMAGING.</p>
  <p class="label lead-unforgettable">UNFORGETTABLE</p>
  <p class="headline word-moments">MOMENTS</p>

  <p class="services services-top"><span class="dot"></span>4D Ultrasound <span class="dot gap"></span>Early Gender</p>
  <p class="services services-bottom"><span class="dot"></span>Pregnancy Confirmation</p>

  <p class="label lead-meet">MEET YOUR</p>
  <p class="headline word-baby">BABY</p>
  <p class="label lead-before">BEFORE</p>
  <p class="headline word-birth">BIRTH</p>

  <div class="phone">
    <svg class="phone-icon" viewBox="0 0 48 48" aria-hidden="true">
      <circle cx="24" cy="24" r="24" fill="var(--gold)"/>
      <path d="M17 12 h7 l-2 8 h-3 c-1 3-1 6 0 9 h3 l2 8 h-7 c-4-4-5-9-5-13 s1-9 5-12 Z" fill="var(--white)" transform="rotate(-12 24 24)"/>
    </svg>
    <span class="phone-number">850-471-3905</span>
  </div>
</section>
</body>
</html>
```